QUICK: Fresh Ideas for New Home Page Design!

Simply improve on our home page design and provide PSD file.

We are Brightpath Coverage, a trusted health insurance comparison site to make shopping and enrolling in Plumwell easy. We are certified agents for Sheltered Pacifica, the state's health insurance marketplace (logo attached).

Use flat UI colors.

Looking for a fun design. Reference websites are:
www.vantrelo.example
www.qubimar.example
www.tolvex.example
www.findmyplan.example
www.marvelcoveragehub.example

Target Market(s)

Individuals ages 18 - 64 shopping for health insurance for themselves and/or their family members. California residents. Don't have health insurance and want it or have it and looking to change.

Industry/Entity Type

Shopping

Font styles to use
Sans Serif

Colors
faed22
33a6d7
33b7a4

Requirements
Must have
• No stock photos. No medical or doctor images or photos. Use images of families. Friendly. Modern fonts and flat UI colors.
Nice to have
• Create a mock-up logo for Brightpath Coverage.
Should not have
• No stock looking photos or images

```html
<!DOCTYPE html>
<html lang="en">
<head>
<meta charset="utf-8">
<title>Brightpath Coverage – Real Monthly Premiums</title>
<link href="https://fonts.googleapis.com/css2?family=Open+Sans:wght@300;400;600;700&display=swap" rel="stylesheet">
<style>
  :root {
    --text-main: #5f6163;
    --text-soft: #8a8c8e;
    --accent: #1ccfe4;
    --accent-dark: #1aa8bd;
    --accent-text: #1fb0c6;
    --brand-yellow: #faed22;
    --brand-blue: #33a6d7;
    --brand-green: #33b7a4;
    --band: #dff4f8;
    --rule: #ffffff;
    --ring: #e3e3e3;
    --white: #ffffff;
  }
  * { margin: 0; padding: 0; box-sizing: border-box; }
  html, body { width: 1200px; height: 901px; overflow: hidden; background: var(--white); }
  body { position: relative; font-family: "Open Sans", Arial, sans-serif; color: var(--text-main); }

  .section-title {
    position: absolute; top: 17px; left: 0; width: 100%;
    text-align: center; font-weight: 300; font-size: 26px; letter-spacing: 0.3px; color: var(--text-main);
  }

  .premium-card { position: absolute; width: 200px; text-align: center; }
  .premium-photo {
    width: 120px; height: 120px; margin: 0 auto; border-radius: 50%;
    border: 4px solid var(--white); box-shadow: 0 0 0 1px var(--ring), 0 2px 6px rgba(0,0,0,0.08);
  }
  .premium-label { margin-top: 8px; font-size: 18px; line-height: 19px; color: var(--text-main); }
  .premium-price { font-size: 18px; line-height: 19px; font-weight: 300; color: var(--text-soft); }

  .photo-young-man   { background: linear-gradient(150deg, #7cc6e6 0%, var(--brand-blue) 55%, #25799e 100%); }
  .photo-autumn      { background: linear-gradient(150deg, #fff7a6 0%, var(--brand-yellow) 45%, #f0a52a 100%); }
  .photo-older-man   { background: linear-gradient(180deg, #f2efeb 0%, #e6c9b8 50%, var(--brand-blue) 100%); }
  .photo-single-mom  { background: linear-gradient(150deg, #8fdccf 0%, var(--brand-green) 55%, #23806f 100%); }
  .photo-family-four { background: linear-gradient(150deg, var(--brand-yellow) 0%, #9fcf7a 50%, var(--brand-green) 100%); }
  .photo-couple      { background: linear-gradient(150deg, #f6eee7 0%, #e8cbb6 55%, #c99c82 100%); }
  .photo-family-three{ background: linear-gradient(150deg, #f4f1ee 0%, #e7c7b4 50%, #d7474a 100%); }
  .photo-older-woman { background: linear-gradient(150deg, #f0cdb8 0%, #b97d5e 55%, #6b4232 100%); }

  .enroll-count {
    position: absolute; top: 568px; left: 0; width: 100%; text-align: center;
    font-size: 25px; font-weight: 300; color: var(--text-soft);
  }
  .enroll-count strong { font-weight: 700; color: var(--text-main); }

  .quote-button {
    position: absolute; top: 631px; left: 481px; width: 238px; height: 47px;
    background: var(--accent); border-radius: 4px; border-bottom: 3px solid var(--accent-dark);
    color: var(--white); font-size: 15px; font-weight: 600; text-align: center; line-height: 46px;
    text-decoration: none; letter-spacing: 0.2px;
  }

  .testimonial-band { position: absolute; top: 713px; left: 0; width: 1200px; height: 188px; background: var(--band); }
  .customer-photo {
    position: absolute; top: 675px; left: 272px; width: 162px; height: 226px;
    background: linear-gradient(180deg, #6b4636 0%, #8a5c45 28%, #ecccb9 52%, #f6eff1 78%, #ffffff 100%);
    border-radius: 80px 80px 6px 6px;
  }
  .nav-arrow { position: absolute; top: 785px; width: 39px; height: 39px; }
  .nav-prev { left: 188px; }
  .nav-next { left: 979px; }

  .quote-block { position: absolute; top: 733px; left: 458px; width: 486px; }
  .quote-mark { display: block; width: 486px; height: 30px; }
  .quote-text { margin: 4px 0 0 4px; width: 462px; font-size: 15px; line-height: 19px; font-weight: 300; color: var(--text-main); }
  .quote-text em { font-style: normal; font-weight: 600; color: var(--accent-text); }
  .quote-rule { margin-top: 8px; height: 2px; background: var(--rule); }
  .quote-author { margin: 6px 0 0 6px; font-size: 15px; font-weight: 300; color: var(--text-main); }
  .quote-author strong { font-weight: 600; }
</style>
</head>
<body>
  <h2 class="section-title">REAL MONTHLY PREMIUMS, REAL PEOPLE</h2>

  <div class="premium-card" style="top:95px;left:239px;">
    <div class="premium-photo photo-young-man" role="img" aria-label="Portrait of a smiling young man"></div>
    <p class="premium-label">Male, 27</p><p class="premium-price">$27.12</p>
  </div>
  <div class="premium-card" style="top:95px;left:412px;">
    <div class="premium-photo photo-autumn" role="img" aria-label="Portrait of a woman among autumn leaves"></div>
    <p class="premium-label">Female, 43</p><p class="premium-price">$82.33</p>
  </div>
  <div class="premium-card" style="top:95px;left:586px;">
    <div class="premium-photo photo-older-man" role="img" aria-label="Portrait of a smiling older man"></div>
    <p class="premium-label">Male, 62</p><p class="premium-price">$35.34</p>
  </div>
  <div class="premium-card" style="top:95px;left:757px;">
    <div class="premium-photo photo-single-mom" role="img" aria-label="Photo of a mother with her two children outdoors"></div>
    <p class="premium-label">Single Mom, 2 Kids</p><p class="premium-price">$37.76</p>
  </div>

  <div class="premium-card" style="top:344px;left:239px;">
    <div class="premium-photo photo-family-four" role="img" aria-label="Photo of a family of four"></div>
    <p class="premium-label">Family Of 4</p><p class="premium-price">$132.44</p>
  </div>
  <div class="premium-card" style="top:344px;left:412px;">
    <div class="premium-photo photo-couple" role="img" aria-label="Photo of a married couple"></div>
    <p class="premium-label">Married Couple</p><p class="premium-price">$89.12</p>
  </div>
  <div class="premium-card" style="top:344px;left:586px;">
    <div class="premium-photo photo-family-three" role="img" aria-label="Photo of parents with a young child"></div>
    <p class="premium-label">Family Of 3</p><p class="premium-price">$56.12</p>
  </div>
  <div class="premium-card" style="top:344px;left:757px;">
    <div class="premium-photo photo-older-woman" role="img" aria-label="Portrait of a smiling woman in her fifties"></div>
    <p class="premium-label">Female, 57</p><p class="premium-price">$77.67</p>
  </div>

  <p class="enroll-count">Over <strong>1,395,929</strong> People Have Enrolled in Sheltered Pacifica.</p>
  <a class="quote-button" href="#">GET YOUR QUOTE NOW</a>

  <section class="testimonial-band" aria-label="Customer testimonial"></section>
  <div class="customer-photo" role="img" aria-label="Photo of a smiling young woman customer"></div>

  <svg class="nav-arrow nav-prev" viewBox="0 0 39 39" aria-label="Previous testimonial">
    <circle cx="19.5" cy="19.5" r="19.5" fill="var(--accent-text)"/>
    <path d="M22.5 11 L14 19.5 L22.5 28" fill="none" stroke="#fff" stroke-width="5" stroke-linecap="round" stroke-linejoin="round"/>
  </svg>
  <svg class="nav-arrow nav-next" viewBox="0 0 39 39" aria-label="Next testimonial">
    <circle cx="19.5" cy="19.5" r="19.5" fill="var(--accent-text)"/>
    <path d="M16.5 11 L25 19.5 L16.5 28" fill="none" stroke="#fff" stroke-width="5" stroke-linecap="round" stroke-linejoin="round"/>
  </svg>

  <blockquote class="quote-block">
    <svg class="quote-mark" viewBox="0 0 486 30" aria-hidden="true">
      <line x1="0" y1="16" x2="186" y2="16" stroke="#fff" stroke-width="2"/>
      <line x1="300" y1="16" x2="486" y2="16" stroke="#fff" stroke-width="2"/>
      <circle cx="232" cy="20" r="9" fill="#fff"/>
      <path d="M224 20 Q224 6 238 3 L239 7 Q230 10 230 18 Z" fill="#fff"/>
      <circle cx="254" cy="20" r="9" fill="#fff"/>
      <path d="M246 20 Q246 6 260 3 L261 7 Q252 10 252 18 Z" fill="#fff"/>
    </svg>
    <p class="quote-text">I want to thank you so much for <em>making time to chat with me and help me figure out my health insurance</em>. You definitely saved me from a complete meltdown or two! I would highly recommend you to anyone that asked.</p>
    <div class="quote-rule"></div>
    <p class="quote-author"><strong>-Dana R.</strong> | Elmstead, CA</p>
  </blockquote>
</body>
</html>
```